Austin TX First Veterinary Urgent Care

We need a flyer designed for us and our clinic that is eye-catching but also summarizes the advantages of our services. We want to express that we are family owned, have convenient hours and affordable prices. We are the first veterinary urgent care animal clinic in Austin Texas. Our hours of operation are M-F 12PM-9PM S-S 10AM-6PM. Our Address is 8715 W Larkmoor Rd Suite B262 Austin, Tx 78699. Our phone number is (737)555-0148 our website is www.brolliepetco.example and our email address is info@brolliepetco.example.

Target Market(s)

Pet owners and veterinary professionals for referral purposes.

Industry/Entity Type

Veterinary

Font styles to use
Sans Serif

Colors
0094D4
00A9DD
6FCCEA
C7EBF8
E9F6FB
00AB8E
00BBA5
67D7C9
C6EFE9
E9F9F6

Requirements
Must have
• Our logo, hours of operation and contact information easy to read. Should emphasize that we are affordable as well as family owned. List of services should also be displayed: ear, eye, and skin issues, limping, broken toenails, lacerations, coughing, sneezing, allergies, vomiting and diarrhea, urinary issues, constipation, snake bites, toxin ingestion, and many many more
Nice to have
• We would like to have a modern feel with drawn/cartoon images, not realistic stock photos of dogs/cats.

```html
<!DOCTYPE html>
<html lang="en">
<head>
<meta charset="utf-8">
<title>Brollie Pet Co – Veterinary Urgent Care Flyer</title>
<link rel="stylesheet" href="https://fonts.googleapis.com/css2?family=Inter:wght@400;500;600;700;800;900&display=swap">
<style>
:root{
  --navy:#2a2a72;
  --navy-deep:#26266b;
  --green:#44ae57;
  --peach:#dcab9c;
  --beige:#ebe8e1;
  --mist:#d6dbd9;
  --sage:#bfcac4;
  --white:#ffffff;
}
*{margin:0;padding:0;box-sizing:border-box}
html,body{width:1200px;height:768px;overflow:hidden;background:var(--navy-deep)}
body{font-family:"Inter",sans-serif;color:var(--navy)}
.stage{position:relative;width:1200px;height:768px;overflow:hidden;background:var(--navy-deep)}
.page{position:absolute;top:31px;width:547px;height:708px;background:var(--white);overflow:hidden}
.page--front{left:42px}
.page--back{left:613px}
.page-bg{position:absolute;inset:0}
.box{position:absolute;z-index:2;background:var(--navy);border-radius:12px;color:var(--white);display:flex;align-items:center;white-space:nowrap}
.box svg{flex:none}

/* front */
.brand{position:absolute;left:30px;top:70px;width:210px;text-align:center}
.brand-row{display:flex;align-items:center;justify-content:center;gap:8px}
.brand-mark{width:22px;height:22px;border-radius:50%;background:var(--green);flex:none}
.brand-name{font-weight:900;font-size:27px;line-height:1;color:var(--navy);letter-spacing:-.5px;white-space:nowrap}
.brand-tag{font-size:8.5px;font-weight:600;letter-spacing:.6px;margin-top:6px;color:var(--navy)}
.hours{left:324px;top:48px;width:179px;height:125px;border-radius:14px;flex-direction:column;justify-content:center;text-align:center;gap:2px}
.hours-day{color:var(--green);font-size:16px;font-weight:500}
.hours-time{font-size:16.5px;font-weight:500}
.hours-rule{width:130px;height:1px;background:rgba(255,255,255,.25);margin:6px 0 8px}
.headline{position:absolute;z-index:2;left:50px;top:262px;font-size:38px;font-weight:900;line-height:40px;color:var(--navy);letter-spacing:-.6px;white-space:nowrap}
.headline em{font-style:normal;color:var(--green);font-size:52px}
.front-phone{left:47px;top:422px;width:231px;height:40px;gap:12px;padding-left:12px;font-size:23px;font-weight:700}
.front-mail{left:47px;top:472px;width:268px;height:40px;gap:14px;padding-left:12px;font-size:15px;font-weight:500}
.front-addr{left:47px;top:522px;width:300px;height:63px;gap:12px;padding-left:14px;font-size:14.5px;font-weight:600;line-height:19px}
.family{position:absolute;z-index:2;left:65px;top:614px;width:100px;text-align:center;color:var(--white);font-weight:800;font-size:17.5px;line-height:22px}
.art{position:absolute;left:0;top:0;z-index:1}

/* back */
.services{position:absolute;left:56px;top:52px;width:434px;height:260px;background:var(--green);border-radius:24px}
.services-title{position:absolute;left:24px;top:18px;width:386px;height:46px;background:var(--navy);border-radius:12px;color:var(--white);font-weight:900;font-size:31px;display:flex;align-items:center;justify-content:center;letter-spacing:-.3px}
.services-list{position:absolute;top:84px;list-style:none;color:var(--white);font-size:12.5px;font-weight:600;letter-spacing:.2px}
.services-list li{height:23.2px;position:relative;padding-left:12px;white-space:nowrap}
.services-list li::before{content:"";position:absolute;left:0;top:5px;width:3px;height:3px;border-radius:50%;background:var(--white)}
.services-list li.plain::before{display:none}
.services-list--a{left:42px}
.services-list--b{left:245px}
.prices{position:absolute;left:40px;top:336px;width:467px;text-align:center}
.prices h2{font-size:21px;font-weight:900;letter-spacing:-.2px}
.prices p{font-size:16px;font-weight:500;line-height:20px;margin-top:2px}
.back-brand{position:absolute;left:110px;top:458px;width:327px;text-align:center}
.back-brand .brand-name{font-size:31px}
.back-phone{left:56px;top:524px;width:206px;height:40px;gap:12px;padding-left:14px;font-size:21px;font-weight:700}
.back-mail{left:270px;top:524px;width:222px;height:40px;gap:9px;padding-left:12px;font-size:13px;font-weight:500}
.back-addr{left:68px;top:574px;width:410px;height:37px;gap:8px;padding-left:18px;font-size:14px;font-weight:600}
.web{position:absolute;left:0;width:547px;top:631px;text-align:center;color:var(--white);font-size:16.5px;font-weight:600}
.web svg{display:block;margin:0 auto 6px}
</style>
</head>
<body>
<main class="stage">

  <section class="page page--front" aria-label="Flyer front">
    <svg class="page-bg" width="547" height="708" viewBox="0 0 547 708" aria-hidden="true">
      <rect x="25" y="24" width="498" height="660" fill="var(--beige)"/>
      <path d="M25 24 H292 C262 170 170 255 25 265 Z" fill="var(--white)"/>
      <path d="M25 370 C200 350 380 300 523 230 V684 H25 Z" fill="var(--mist)"/>
      <path d="M25 585 C150 570 240 600 300 684 H25 Z" fill="var(--green)"/>
      <circle cx="0" cy="0" r="62" fill="var(--peach)"/>
    </svg>

    <svg class="art" width="547" height="708" viewBox="0 0 547 708" role="img" aria-label="Cartoon illustration of a smiling veterinarian in green scrubs with a stethoscope petting a golden dog">
      <defs>
        <linearGradient id="artTone" x1="0" y1="0" x2="0.4" y2="1">
          <stop offset="0" stop-color="#2a2a72"/>
          <stop offset="0.45" stop-color="#44ae57"/>
          <stop offset="1" stop-color="#d6a18e"/>
        </linearGradient>
      </defs>
      <path d="M395 345 C420 320 480 315 547 335 V708 H262 C262 640 290 590 330 560 C365 530 385 470 392 420 Z" fill="url(#artTone)" opacity=".92"/>
    </svg>

    <div class="brand">
      <div class="brand-row"><span class="brand-mark"></span><span class="brand-name">Brollie Pet Co</span></div>
      <div class="brand-tag">VETERINARY URGENT CARE</div>
    </div>

    <div class="box hours">
      <div class="hours-day">Monday-Friday</div>
      <div class="hours-time">12:00pm-9:00pm</div>
      <div class="hours-rule"></div>
      <div class="hours-day">Saturday-Sunday</div>
      <div class="hours-time">10:00am-6:00pm</div>
    </div>

    <h1 class="headline">Getting Austin's<br>pets back on their<br>paws, <em>ASAP</em></h1>

    <div class="box front-phone">
      <svg width="22" height="22" viewBox="0 0 24 24" aria-hidden="true"><path d="M6.6 10.8a15 15 0 0 0 6.6 6.6l2.2-2.2a1 1 0 0 1 1-.25 11.4 11.4 0 0 0 3.6.57 1 1 0 0 1 1 1V20a1 1 0 0 1-1 1A17 17 0 0 1 3 4a1 1 0 0 1 1-1h3.5a1 1 0 0 1 1 1c0 1.250.2 2.450.57 3.57a1 1 0 0 1-.25 1z" fill="var(--green)"/></svg>
      (737)555-0148
    </div>
    <div class="box front-mail">
      <svg width="24" height="18" viewBox="0 0 24 18" aria-hidden="true"><rect x="1" y="1" width="22" height="16" fill="none" stroke="var(--green)" stroke-width="1.6"/><path d="M1 1 L12 10 L23 1 M1 17 L9 8 M23 17 L15 8" fill="none" stroke="var(--green)" stroke-width="1.6"/></svg>
      info@brolliepetco.example
    </div>
    <div class="box front-addr">
      <svg width="18" height="26" viewBox="0 0 18 26" aria-hidden="true"><path d="M9 0a9 9 0 0 0-9 9c0 7 9 17 9 17s9-10 9-17a9 9 0 0 0-9-9zm0 12.5A3.5 3.5 0 1 1 9 5.5a3.5 3.5 0 0 1 0 7z" fill="var(--green)"/></svg>
      <span>8715 W Larkmoor Rd Suite B262<br>Austin, Tx 78699</span>
    </div>

    <div class="family">FAMILY<br>OWNED</div>
  </section>

  <section class="page page--back" aria-label="Flyer back">
    <svg class="page-bg" width="547" height="708" viewBox="0 0 547 708" aria-hidden="true">
      <rect x="24" y="24" width="499" height="660" fill="var(--sage)"/>
      <path d="M24 24 H420 C300 150 120 250 24 270 Z" fill="var(--peach)"/>
      <path d="M523 170 C420 190 320 260 230 310 C150 360 80 440 24 560 V684 H523 Z" fill="var(--mist)"/>
      <path d="M523 340 C400 380 300 450 270 560 H523 Z" fill="var(--beige)"/>
      <path d="M523 560 C480 580 455 620 450 684 H523 Z" fill="var(--peach)"/>
      <path d="M0 660 C120 610 260 600 340 610 C440 622 500 660 547 708 H0 Z" fill="var(--green)"/>
    </svg>

    <div class="services">
      <h2 class="services-title">OUR SERVICES</h2>
      <ul class="services-list services-list--a">
        <li>EAR,EYE, &amp; SKIN ISSUES</li>
        <li>LIMPING</li>
        <li>BROKEN TOENAILS</li>
        <li>LACERATIONS</li>
        <li>COUGHING</li>
        <li>SNEEZING</li>
        <li>ALLERGIES</li>
      </ul>
      <ul class="services-list services-list--b">
        <li>VOMITING &amp; DIARRHEA</li>
        <li>URINARY ISSUES</li>
        <li>CONSTIPATION</li>
        <li>SNAKE BITES</li>
        <li>TOXIN INGESTION</li>
        <li class="plain">&amp; MANY MANY MORE</li>
      </ul>
    </div>

    <div class="prices">
      <h2>AFFORDABLE PRICES</h2>
      <p>Urgent Care veterinary services at a fraction of<br>the cost of an Emergency visit.</p>
    </div>

    <div class="back-brand brand">
      <div class="brand-row"><span class="brand-mark"></span><span class="brand-name">Brollie Pet Co</span></div>
      <div class="brand-tag">VETERINARY URGENT CARE</div>
    </div>

    <div class="box back-phone">
      <svg width="20" height="20" viewBox="0 0 24 24" aria-hidden="true"><path d="M6.6 10.8a15 15 0 0 0 6.6 6.6l2.2-2.2a1 1 0 0 1 1-.25 11.4 11.4 0 0 0 3.6.57 1 1 0 0 1 1 1V20a1 1 0 0 1-1 1A17 17 0 0 1 3 4a1 1 0 0 1 1-1h3.5a1 1 0 0 1 1 1c0 1.250.2 2.450.57 3.57a1 1 0 0 1-.25 1z" fill="var(--green)"/></svg>
      (737)555-0148
    </div>
    <div class="box back-mail">
      <svg width="20" height="15" viewBox="0 0 24 18" aria-hidden="true"><rect x="1" y="1" width="22" height="16" fill="none" stroke="var(--green)" stroke-width="1.6"/><path d="M1 1 L12 10 L23 1 M1 17 L9 8 M23 17 L15 8" fill="none" stroke="var(--green)" stroke-width="1.6"/></svg>
      info@brolliepetco.example
    </div>
    <div class="box back-addr">
      <svg width="13" height="18" viewBox="0 0 18 26" aria-hidden="true"><path d="M9 0a9 9 0 0 0-9 9c0 7 9 17 9 17s9-10 9-17a9 9 0 0 0-9-9zm0 12.5A3.5 3.5 0 1 1 9 5.5a3.5 3.5 0 0 1 0 7z" fill="var(--green)"/></svg>
      8715 W Larkmoor Rd Suite B262 Austin, Tx 78699
    </div>

    <div class="web">
      <svg width="20" height="20" viewBox="0 0 20 20" aria-hidden="true"><g fill="none" stroke="var(--navy)" stroke-width="1.4"><circle cx="10" cy="10" r="8.5"/><ellipse cx="10" cy="10" rx="3.8" ry="8.5"/><path d="M1.5 10h17M3 5.5h14M3 14.5h14"/></g></svg>
      www.brolliepetco.example
    </div>
  </section>

</main>
</body>
</html>
```